Clone http://www.pebbledeskwriter.com/ (fully functioning WordPress website - not just design)

1) Clone or recreate http://www.pebbledeskwriter.com/ in Wordpress with WooCommerece plugin
2) Connect to our Existing Quendo Account
3) Make site-wide text only changes that we provide you when site is complete.

We will provide all the graphics according to your size requirements.

Cash awarded to the closest copy of http://www.pebbledeskwriter.com/

Target Market(s)

WordPress developer

Number of Pages Required

5+ page

Font styles to use
Sans Serif

Colors
abd037
cadf82
eaf2ce

Requirements
Must have
• Fully functioning website.

```html
<!DOCTYPE html>
<html lang="en">
<head>
<meta charset="utf-8">
<title>Pebbledesk Writer — Easy, Online Mail Merge</title>
<link rel="stylesheet" href="https://fonts.googleapis.com/css2?family=Dosis:wght@200;300;400&family=Open+Sans:wght@400;600;700&display=swap">
<style>
:root{
  --green:#abd037;
  --green-mid:#5bb833;
  --green-dark:#3e8f1e;
  --green-pale:#cadf82;
  --green-wash:#eaf2ce;
  --topbar:#1b1b1b;
  --wood-dark:#2a0f08;
  --wood:#5a2414;
  --band:#383746;
  --footer:#e4e4e4;
  --footer-base:#cfcfcf;
  --ink:#333;
  --ink-soft:#555;
  --heading-green:#6fc13f;
  --sky:#bfe5f6;
}
*{box-sizing:border-box;margin:0;padding:0}
html,body{width:954px;height:1200px;overflow:hidden}
body{position:relative;background:#fff;font-family:"Open Sans",Arial,sans-serif;color:var(--ink)}
.abs{position:absolute}

/* top bar */
.topbar{left:0;top:0;width:954px;height:25px;background:var(--topbar);border-bottom:1px solid #2d4c8a}
.topbar-note{left:198px;top:6px;font-size:7.5px;color:#ddd}
.topbar-cart{left:641px;top:6px;font-size:7.5px;color:#eee;display:flex;align-items:center;gap:4px}
.topbar-search{left:689px;top:7px}
.login{left:708px;top:4px;width:48px;height:16px;background:linear-gradient(#4f8ef0,#2a63d0);color:#fff;font-size:7.5px;text-align:center;line-height:16px;border-radius:2px}

/* hero */
.hero{left:0;top:25px;width:954px;height:281px;background:radial-gradient(ellipse at 58% 45%,#7a3a1e 0%,var(--wood) 35%,var(--wood-dark) 100%)}
.brand{left:250px;top:36px;display:flex;align-items:center;gap:12px}
.brand-mark{width:30px;height:30px;border-radius:50%;background:var(--green)}
.brand-name{font-family:"Dosis",sans-serif;font-weight:300;font-size:16px;color:#f0e6df}
.nav{left:494px;top:41px;display:flex;gap:3px}
.nav a{display:block;height:23px;padding:0 9px;background:#1f1f1f;color:#eee;font-size:6.5px;font-weight:600;line-height:23px;text-decoration:none;border:1px solid #333}
.nav a.is-current{border-bottom:2px solid var(--green-mid)}
.hero-title{left:248px;top:86px;font-family:"Dosis",sans-serif;font-weight:400;font-size:35px;line-height:48px;color:#fff}
.btn{display:block;background:linear-gradient(#7dd04a,var(--green-dark));color:#fff;text-align:center;font-weight:600;border:1px solid #2f7a16;border-radius:2px}
.hero-btn{left:250px;top:198px;width:143px;height:20px;font-size:8.5px;line-height:18px}
.hero-sub{left:250px;top:221px;font-size:7.5px;color:#a88}
.hero-art{left:405px;top:90px;width:335px;height:150px;border-radius:6px;background:radial-gradient(ellipse at 40% 50%,#c9c5c0 0%,#6b5a50 45%,rgba(60,25,12,0) 75%)}
.hero-q{left:248px;top:247px;font-size:10.5px;color:var(--green)}
.hero-text{left:248px;top:261px;width:460px;font-size:7.6px;line-height:14.5px;color:#f3ece8;text-align:justify}

/* features */
.features{left:0;top:306px;width:954px;height:689px;background:linear-gradient(135deg,#eef1f5 0%,#fafbfc 40%,#f0f3f6 70%,#fff 100%)}
.section-title{left:0;top:336px;width:954px;text-align:center;font-family:"Dosis",sans-serif;font-weight:300;font-size:27px;color:#333}
.title-rule{left:405px;top:381px;width:144px;height:2px;background:var(--green-dark)}
.step-head{display:flex;align-items:center;gap:4px;font-family:"Dosis",sans-serif;font-weight:200;font-size:24px;color:var(--heading-green)}
.step-num{width:18px;height:18px;border-radius:50%;background:var(--green-dark);color:#fff;font-family:"Open Sans",sans-serif;font-size:9px;font-weight:600;text-align:center;line-height:18px}
.step-lead{font-size:7.5px;font-weight:600;color:#222;margin-top:14px}
.step-body{font-size:7.6px;line-height:14.4px;color:var(--ink-soft);margin-top:3px}
.step-art{background:linear-gradient(#fff 30%,var(--sky) 100%)}
.screen-art{background:linear-gradient(#3a3a3a 0 8px,#f2f2f2 8px);border:1px solid #999}
.divider{left:290px;width:380px;height:1px;background:linear-gradient(90deg,transparent,#c8c8c8,transparent)}

/* call band */
.band{left:0;top:995px;width:954px;height:115px;background:var(--band)}
.band-notch{left:441px;top:980px}
.band-btn{left:405px;top:1036px;width:145px;height:29px;font-size:11px;line-height:27px;font-weight:400;border:2px solid #bfe3a8}
.band-text{left:0;top:1075px;width:954px;text-align:center;font-size:11px;color:#fff}

/* footer */
.footer{left:0;top:1110px;width:954px;height:72px;background:var(--footer)}
.foot-head{left:200px;top:1120px;font-size:7.5px;font-weight:700;color:#222}
.foot-link{font-size:6px;font-weight:700;color:#222}
.foot-sep{top:1118px;width:1px;height:50px;background:#ccc}
.social{top:1132px;width:26px;height:26px;border-radius:50%;background:linear-gradient(#72c33e,var(--green-dark))}
.social svg{display:block}
.credit{left:603px;top:1120px;width:100px;font-size:5.5px;line-height:7.5px;color:#333;border-top:1px solid #999}
.credit strong{font-weight:700}
.base{left:0;top:1182px;width:954px;height:18px;background:var(--footer-base)}
.copyright{left:248px;top:1186px;font-size:5.5px;color:#444}
</style>
</head>
<body>

<div class="abs topbar"></div>
<div class="abs topbar-note">Lorem Ipsum is simply dummy text of</div>
<div class="abs topbar-cart">
  <svg width="7" height="7" viewBox="0 0 7 7"><path d="M1 2h5l-.5 5h-4z M2.3 2V1.3a1.2 1.2 0 0 1 2.4 0V2" fill="#eee" stroke="#eee" stroke-width=".6"/></svg>
  CART ($0)
</div>
<svg class="abs topbar-search" width="8" height="8" viewBox="0 0 8 8"><circle cx="3.2" cy="3.2" r="2.3" fill="none" stroke="#eee" stroke-width="1.2"/><path d="M5 5l2.4 2.4" stroke="#eee" stroke-width="1.4"/></svg>
<div class="abs login">Login</div>

<header class="abs hero"></header>
<div class="abs brand"><span class="brand-mark"></span><span class="brand-name">Pebbledesk Writer</span></div>
<nav class="abs nav">
  <a class="is-current">Home</a><a>Tour</a><a>Price</a><a>Our Team</a><a>Contact Us</a>
</nav>
<h1 class="abs hero-title">Easy, Online<br>Mail Merge</h1>
<a class="abs btn hero-btn">Start a Free Trial</a>
<div class="abs hero-sub">Start building your mail merge online now!</div>
<div class="abs hero-art" role="img" aria-label="Desk scene with a laptop, coffee cup, graphics tablet and papers"></div>
<div class="abs hero-q">Do you have a letter you need to send out to multiple people?</div>
<p class="abs hero-text">Mail merge is the automatic addition of names and addresses from a spreadsheet to letters and envelopes in order to facilitate sending personalised mail to many people.</p>

<section class="abs features"></section>
<h2 class="abs section-title">100% Easier Than Using a Desktop Word Processor!</h2>
<div class="abs title-rule"></div>

<div class="abs" style="left:198px;top:412px;width:316px">
  <div class="step-head"><span class="step-num">1</span>Upload Your Data</div>
  <p class="step-lead">Create a list of addresses, names or other data</p>
  <p class="step-body">Just copy and paste or type your data about your clients such as their name, address and any other associated fields into our in browser spreadsheet. You can even upload your data as a CSV file! It couldn't be easier. Your data is easy to manage and best yet, it's all backed up in the cloud.</p>
</div>
<div class="abs step-art" style="left:543px;top:416px;width:213px;height:120px" role="img" aria-label="Illustration of a cloud syncing data with a phone and a laptop"></div>
<div class="abs divider" style="top:566px"></div>

<div class="abs screen-art" style="left:198px;top:599px;width:213px;height:122px" role="img" aria-label="Screenshot of the template editor with an envelope layout"></div>
<div class="abs" style="left:436px;top:597px;width:322px">
  <div class="step-head"><span class="step-num">2</span>Design Your Template</div>
  <p class="step-lead">Build your document in your browser, it's easy</p>
  <p class="step-body">You can build any document in our easy to use editor. Choose from a range of paper sizes like A4, C4 Envelope, US Letter or specify your own. Drag and drop the variables from your uploaded data right onto your page. Scan or upload an existing PDF or DocX document to be used as your page background. Best of all you can reuse the template again and again.</p>
</div>
<div class="abs divider" style="top:752px"></div>

<div class="abs" style="left:198px;top:788px;width:320px">
  <div class="step-head"><span class="step-num">3</span>Merge to PDF</div>
  <p class="step-lead">Combine it all into a PDF ready for print</p>
  <p class="step-body">We'll automatically combine your data with your template, producing a unique page or set of pages for each row. Then it's easy to print off your PDF and mail out your pages. You can create anything from personally addressed advertising to invoices and pre filled forms.</p>
</div>
<div class="abs step-art" style="left:542px;top:792px;width:213px;height:120px" role="img" aria-label="Illustration of a cloud syncing data with a phone and a laptop"></div>
<div class="abs divider" style="top:942px"></div>

<section class="abs band"></section>
<svg class="abs band-notch" width="72" height="16" viewBox="0 0 72 16"><path d="M0 16L36 0L72 16Z" fill="var(--band)"/><path d="M18 16L36 8L54 16Z" fill="#fff"/></svg>
<a class="abs btn band-btn">Start a Free Trial</a>
<div class="abs band-text">Start building your mail merge online now!</div>

<footer class="abs footer"></footer>
<div class="abs foot-head">Browse</div>
<div class="abs foot-link" style="left:200px;top:1139px">Privacy Policy</div>
<div class="abs foot-link" style="left:200px;top:1154px">Terms &amp; Conditions</div>
<div class="abs foot-link" style="left:332px;top:1139px">Refund Policy</div>
<div class="abs foot-sep" style="left:404px"></div>
<div class="abs social" style="left:435px" role="img" aria-label="Community chat link">
  <svg width="26" height="26" viewBox="0 0 26 26"><path d="M8 9h10v6.5h-6l-3 2.5v-2.5h-1z" fill="#fff"/></svg>
</div>
<div class="abs social" style="left:469px" role="img" aria-label="Share link">
  <svg width="26" height="26" viewBox="0 0 26 26"><path d="M10 13L16 9.5M10 13L16 16.5" stroke="#fff" stroke-width="1.2"/><circle cx="10" cy="13" r="2" fill="#fff"/><circle cx="16" cy="9.5" r="2" fill="#fff"/><circle cx="16" cy="16.5" r="2" fill="#fff"/></svg>
</div>
<div class="abs social" style="left:503px" role="img" aria-label="Email us">
  <svg width="26" height="26" viewBox="0 0 26 26"><rect x="8" y="9.5" width="10" height="7" fill="#fff"/><path d="M8 9.5l5 4 5-4" fill="none" stroke="#5bb833" stroke-width=".8"/></svg>
</div>
<div class="abs foot-sep" style="left:561px"></div>
<div class="abs credit">PW was created by<br><strong>Tern Works</strong><br>PO Box 2217, Harbour Rise, 4110, Qld<br>Australia</div>
<div class="abs base"></div>
<div class="abs copyright">© Copyright 2017 Tern Works, All Rights Reserved</div>

</body>
</html>
```